RWT General Contracting

Roofing, Siding,windows, doors, Gutter,additions, decks, garagesand hanyman services fully insured and licensed, free estimates, accept all major credit cards call (617)442-9073 email morvinkt@mailbrook.net

Target Market(s)

Home improvement

Industry/Entity Type

Home Improvement

Requirements
Must have
• Whats listed above
Nice to have
• I dont have a logo i want wording for roofing, siding, gutter, decks, additions, windows, doors, and handyman services with my phone # 617-442-9073 and email morvinkt@mailbrook.net

```html
<!DOCTYPE html>
<html lang="en">
<head>
<meta charset="utf-8">
<title>RWT General Contracting – Postcard</title>
<link rel="stylesheet" href="https://fonts.googleapis.com/css2?family=Open+Sans:wght@400;600;700&family=Roboto+Condensed:wght@700&display=swap">
<style>
:root{
  --navy:#1f2a6e;
  --navy-deep:#17205a;
  --navy-light:#2f4296;
  --red:#a4262c;
  --red-bright:#e2392e;
  --grey-text:#6a6a6a;
  --grey-line:#b9bcc4;
  --paper:#ffffff;
  --canvas:#ececec;
}
*{box-sizing:border-box;margin:0;padding:0}
html,body{width:1040px;height:1200px;overflow:hidden;background:var(--canvas)}
body{position:relative;font-family:"Open Sans",Arial,sans-serif}
.card{position:absolute;width:656px;height:506px;background:var(--paper);overflow:hidden;box-shadow:0 2px 6px rgba(0,0,0,.18)}
.card--front{left:90px;top:64px}
.card--back{left:194px;top:630px}
.brand{position:absolute;font-family:"Roboto Condensed",Arial,sans-serif;font-weight:700;color:var(--navy);line-height:1.02;text-transform:uppercase}
.abs{position:absolute}
.cond{font-family:"Roboto Condensed",Arial,sans-serif;font-weight:700}

/* front */
.front-tagline{right:20px;top:72px;font-size:13px;color:var(--grey-text)}
.front-panel{left:0;top:100px;width:656px;height:406px;background:linear-gradient(90deg,var(--navy-light),var(--navy-deep) 55%,var(--navy))}
.hero-photo{left:362px;top:100px;width:294px;height:263px;clip-path:polygon(66px 0,100% 0,100% 100%,0 100%);background:linear-gradient(160deg,#8b8a84 0%,#b3b4b0 40%,#9a9c98 70%,#5e7440 100%)}
.services-tab{left:0;top:146px;width:193px;height:37px;background:linear-gradient(90deg,#fff,#e3e4e8);border-radius:0 6px 6px 0;box-shadow:2px 2px 4px rgba(0,0,0,.3);color:var(--red);font-size:19px;line-height:37px;padding-left:18px}
.service-list{list-style:none;color:#fff;font-size:18px}
.service-list li{height:31px;line-height:31px;position:relative;padding-left:17px}
.service-list li::before{content:"";position:absolute;left:0;top:11px;width:9px;height:9px;border-radius:50%;background:#b9c0d6;box-shadow:inset 0 0 0 2px #5a6690}
.col-1{left:33px;top:206px}
.col-2{left:177px;top:206px}
.thumb{position:absolute;z-index:2;border:3px solid #fff;border-radius:8px;transform:skewX(-8deg);box-shadow:1px 2px 4px rgba(0,0,0,.45)}
.call-band{left:352px;top:363px;width:304px;height:76px;clip-path:polygon(18px 0,100% 0,100% 100%,0 100%);background:linear-gradient(90deg,#fff,#eceef1 60%,#d6d8dd)}
.call-label{right:22px;top:370px;font-size:15px;color:var(--red)}
.call-phone{right:20px;top:388px;font-size:31px;line-height:40px;color:var(--red);display:flex;align-items:center;gap:10px}
.email-band{left:300px;top:439px;width:356px;height:42px;background:linear-gradient(90deg,rgba(255,255,255,0),rgba(190,196,210,.55))}
.front-email{right:24px;top:447px;color:#fff;font-size:20px;font-weight:600;letter-spacing:.3px}

/* back */
.return-address{left:372px;top:32px;font-size:11.5px;line-height:17px;color:#555}
.return-address strong{color:#222;font-weight:700}
.stamp-box{left:550px;top:26px;width:87px;height:61px;border:1.5px solid #9a9a9a}
.address-line{left:392px;width:245px;height:1.5px;background:var(--grey-line)}
.back-panel{left:0;top:139px;width:416px;height:292px;clip-path:polygon(0 0,343px 0,100% 100%,0 100%);background:linear-gradient(90deg,var(--navy-light),var(--navy-deep))}
.back-intro{left:15px;top:158px;width:330px;color:#fff;font-size:13px;line-height:18.5px;font-weight:700;font-family:"Roboto Condensed",Arial,sans-serif}
.licensed-tab{left:0;top:346px;width:206px;height:38px;background:linear-gradient(90deg,#fff,#dfe1e6);border-radius:0 6px 6px 0;box-shadow:2px 2px 4px rgba(0,0,0,.3);color:var(--navy);font-size:16px;line-height:38px;padding-left:22px;font-weight:600}
.cards-note{left:22px;top:400px;color:#fff;font-size:15px;font-weight:600;letter-spacing:-.2px;white-space:nowrap}
.size-badge{left:286px;top:356px;width:100px;height:100px;border-radius:50%;background:var(--red-bright);border:7px solid #b3262b;box-shadow:1px 2px 5px rgba(0,0,0,.45);color:#fff;font-size:12px;line-height:14px;text-align:center;display:flex;align-items:center;justify-content:center;text-transform:uppercase;z-index:2}
.bottom-band{left:0;top:431px;width:448px;height:76px;clip-path:polygon(0 0,416px 0,100% 100%,0 100%);background:linear-gradient(90deg,#fff 55%,#e4e5e9 80%,#b9bcc3)}
.back-call-label{left:29px;top:445px;font-size:11px;color:var(--red)}
.back-phone{left:29px;top:462px;font-size:23px;color:var(--red);display:flex;align-items:center;gap:6px}
.back-email{left:230px;top:466px;font-size:18px;color:var(--navy);font-weight:600}
</style>
</head>
<body>

<section class="card card--front">
  <div class="brand" style="left:18px;top:26px;font-size:24px;width:180px">RWT General<br>Contracting</div>
  <div class="abs cond front-tagline">FULLY INSURED AND LICENSED</div>

  <div class="abs front-panel"></div>
  <div class="abs hero-photo" role="img" aria-label="Photo of a hand driving screws into grey deck boards with a cordless drill"></div>

  <div class="abs cond services-tab">SERVICES OFFERED:</div>
  <ul class="abs service-list col-1">
    <li>Roofing</li><li>Siding</li><li>Windows</li><li>Doors</li><li>Gutter</li>
  </ul>
  <ul class="abs service-list col-2">
    <li>Additions</li><li>Decks</li><li>Garagesand</li><li>Hanyman services</li><li>and much more...</li>
  </ul>

  <div class="abs call-band"></div>
  <div class="abs cond call-label">CALL US NOW FOR A FREE ESTIMATE!</div>
  <div class="abs cond call-phone">
    <svg width="30" height="30" viewBox="0 0 30 30" aria-hidden="true"><path d="M15 3a12 12 0 1 1-9.5 19.3L3 27l4.6-2.2" fill="none" stroke="currentColor" stroke-width="2.6" stroke-linejoin="round"/><path d="M10.5 9.5l2.5-1 2 4-1.6 1.2a7 7 0 0 0 3 3l1.2-1.6 4 2-1 2.5c-4.5.5-10.6-5.6-10.1-10.1z" fill="currentColor"/></svg>
    <span>(617)442-9073</span>
  </div>
  <div class="abs email-band"></div>
  <div class="abs front-email">morvinkt@mailbrook.net</div>

  <div class="thumb" style="left:22px;top:400px;width:113px;height:72px;background:linear-gradient(135deg,#6d5a4a,#a58c74 50%,#4a4038)" role="img" aria-label="Photo of a hammer nailing roof shingles"></div>
  <div class="thumb" style="left:139px;top:400px;width:113px;height:72px;background:linear-gradient(135deg,#8a7a68,#b8a690 50%,#7d6c5a)" role="img" aria-label="Photo of a ladder against shingled roof"></div>
  <div class="thumb" style="left:256px;top:400px;width:113px;height:72px;background:linear-gradient(135deg,#a23a3a,#c7c3bd 55%,#8b8d94)" role="img" aria-label="Photo of a worker installing siding"></div>
</section>

<section class="card card--back">
  <div class="brand" style="left:54px;top:30px;font-size:34px;width:220px">RWT General<br>Contracting</div>

  <div class="abs return-address"><strong>RWT General Contracting</strong><br>14 Linden Lane<br>Westbrook Falls, MA 02700</div>
  <div class="abs stamp-box"></div>
  <div class="abs address-line" style="top:183px"></div>
  <div class="abs address-line" style="top:218px"></div>
  <div class="abs address-line" style="top:253px"></div>
  <div class="abs address-line" style="top:288px"></div>

  <div class="abs back-panel"></div>
  <p class="abs back-intro">Your home is the most important asset you have,<br>so when you're ready to build or remodel, get yourself<br>the best General Contractor in the business!</p>

  <div class="thumb" style="left:17px;top:241px;width:111px;height:74px;background:linear-gradient(135deg,#9ea4ad,#e1e3e6 50%,#6e747c)" role="img" aria-label="Photo of a house with a new garage door"></div>
  <div class="thumb" style="left:132px;top:241px;width:111px;height:74px;background:linear-gradient(135deg,#4b5560,#c9ccd0 50%,#7a828a)" role="img" aria-label="Photo of a gutter guard being installed"></div>
  <div class="thumb" style="left:247px;top:241px;width:111px;height:74px;background:linear-gradient(135deg,#c8d0d8,#f2f4f6 50%,#9aa3ad)" role="img" aria-label="Photo of new white window frames"></div>

  <div class="abs licensed-tab">LICENSED &amp; INSURED</div>
  <div class="abs cards-note">We accept all major credit cards!</div>

  <div class="abs bottom-band"></div>
  <div class="abs cond size-badge">No job is<br>too big or<br>too small</div>
  <div class="abs cond back-call-label">CALL US NOW FOR A FREE ESTIMATE!</div>
  <div class="abs cond back-phone">
    <svg width="24" height="24" viewBox="0 0 30 30" aria-hidden="true"><path d="M15 3a12 12 0 1 1-9.5 19.3L3 27l4.6-2.2" fill="none" stroke="currentColor" stroke-width="2.8" stroke-linejoin="round"/><path d="M10.5 9.5l2.5-1 2 4-1.6 1.2a7 7 0 0 0 3 3l1.2-1.6 4 2-1 2.5c-4.5.5-10.6-5.6-10.1-10.1z" fill="currentColor"/></svg>
    <span>(617)442-9073</span>
  </div>
  <div class="abs back-email">morvinkt@mailbrook.net</div>
</section>

</body>
</html>
```